Business Card Lyle/Tamsin

We would like you to design a business card with the same graphics as the rack card, which is attached, along with our logo. We are looking for a business card for our company director Lyle Barnaby and for myself (Tamsin de Vroomhuis, General Manager).
Updates

Project Deadline Extended
Reason: We did not provide all relevant information before the end of the original deadline. The brief has now been updated and the deadline extended.

Industry/Entity Type

Business

Requirements
Must have
• We need the logo and the following contact details:

Lyle Barnaby
Company Director
17 Pikerton Lane
Wiriana, Auckland, 2046
E: lyle@harbourlinkpf.co.nz
W: www.harbourlinkpf.co.nz
P: +64 (0)9 4813907
F: +64 (0)9 4813905
M: +64 (0)21 968014
FREE: 0508 391046 (NZ only)

Tamsin de Vroomhuis
General Manager
17 Pikerton Lane
Wiriana, Auckland, 2046
E: tamsin@harbourlinkpf.co.nz
W: www.harbourlinkpf.co.nz
P: +64 (0)9 4813907
F: +64 (0)9 4813905
M: +64 (0)21 968015

The phrase "Service Excellence".
Nice to have
• We would like to incorporate icons to indicate "phone", "website", "mobile" etc.

```html
<!DOCTYPE html>
<html lang="en">
<head>
<meta charset="utf-8">
<title>Harbourlink PF – Business Card</title>
<link rel="stylesheet" href="https://fonts.googleapis.com/css2?family=Poppins:wght@500;600&family=Quicksand:wght@400;500;600&display=swap">
<style>
  :root {
    --brand-blue: #1c3fb0;
    --brand-red: #d3283a;
    --card-white: #f6f6f4;
    --stage: #e4e4e4;
    --ink-light: #ffffff;
  }
  * { box-sizing: border-box; margin: 0; padding: 0; }
  html, body { width: 1200px; height: 1000px; overflow: hidden; }
  body {
    background: var(--stage);
    font-family: "Quicksand", sans-serif;
    display: flex;
    flex-direction: column;
    align-items: center;
    justify-content: center;
    gap: 60px;
  }
  .card {
    position: relative;
    width: 700px;
    height: 400px;
    background: var(--card-white);
    box-shadow: 0 6px 20px rgba(0,0,0,0.15);
    overflow: hidden;
  }
  .card-art { position: absolute; inset: 0; width: 100%; height: 100%; }

  /* Front */
  .person { position: absolute; left: 42px; top: 50px; }
  .person-name {
    font-family: "Poppins", sans-serif;
    font-weight: 600;
    font-size: 36px;
    color: var(--brand-blue);
    line-height: 1.1;
  }
  .person-title { font-size: 17px; color: var(--brand-red); font-weight: 500; }
  .brand-mark {
    position: absolute;
    right: 34px;
    top: 112px;
    font-family: "Poppins", sans-serif;
    font-weight: 600;
    font-size: 26px;
    color: var(--ink-light);
    letter-spacing: 0.5px;
  }
  .contact-list {
    position: absolute;
    left: 42px;
    top: 250px;
    color: var(--ink-light);
    font-size: 16px;
    font-weight: 500;
    display: flex;
    flex-direction: column;
    gap: 12px;
  }
  .contact-row { display: flex; align-items: center; gap: 22px; }
  .contact-item { display: flex; align-items: center; gap: 9px; line-height: 1.2; }
  .icon { width: 18px; height: 18px; flex: none; }

  /* Back */
  .back-brand {
    position: absolute;
    top: 92px;
    width: 100%;
    text-align: center;
    font-family: "Poppins", sans-serif;
    font-weight: 600;
    font-size: 38px;
    color: var(--brand-blue);
  }
  .back-web {
    position: absolute;
    top: 160px;
    width: 100%;
    text-align: center;
    color: var(--brand-blue);
    font-size: 15px;
    letter-spacing: 6px;
  }
  .back-tollfree {
    position: absolute;
    top: 190px;
    width: 100%;
    text-align: center;
    color: var(--brand-red);
  }
  .tollfree-label { font-size: 15px; font-weight: 500; letter-spacing: 0.5px; }
  .tollfree-number { font-size: 36px; font-weight: 500; line-height: 1.1; }
  .tagline { font-family: "Quicksand", sans-serif; font-size: 16px; font-weight: 600; fill: var(--ink-light); letter-spacing: 1px; }
</style>
</head>
<body>

<section class="card card-front">
  <svg class="card-art" viewBox="0 0 700 400" aria-hidden="true">
    <path d="M0 188 Q 380 140 640 0 L700 0 L700 400 L0 400 Z" fill="var(--brand-blue)"/>
    <path d="M0 208 Q 400 162 700 22 L700 400 L0 400 Z" fill="var(--brand-red)"/>
  </svg>

  <div class="person">
    <p class="person-name">Lyle Barnaby</p>
    <p class="person-title">Company Director</p>
  </div>

  <p class="brand-mark">HARBOURLINK PF</p>

  <div class="contact-list">
    <div class="contact-item">
      <svg class="icon" viewBox="0 0 24 24"><path d="M12 2a7 7 0 0 0-7 7c0 5 7 13 7 13s7-8 7-13a7 7 0 0 0-7-7zm0 9.5A2.5 2.5 0 1 1 12 6.5a2.5 2.5 0 0 1 0 5z" fill="#fff"/></svg>
      <span>17 Pikerton Lane<br>Wiriana, Auckland, 2046</span>
    </div>
    <div class="contact-item">
      <svg class="icon" viewBox="0 0 24 24"><rect x="2" y="5" width="20" height="14" rx="1.5" fill="#fff"/><path d="M3 6l9 7 9-7" stroke="var(--brand-red)" stroke-width="1.8" fill="none"/></svg>
      <span>lyle@harbourlinkpf.co.nz</span>
    </div>
    <div class="contact-row">
      <div class="contact-item">
        <svg class="icon" viewBox="0 0 24 24"><circle cx="12" cy="12" r="11" fill="#fff"/><path d="M8.5 6.5l2 2.5-1.2 1.6a8 8 0 0 0 4 4l1.6-1.2 2.5 2-1.3 2c-4.6 0-9-4.4-9-9z" fill="var(--brand-red)"/></svg>
        <span>+64 (0)9 4813907</span>
      </div>
      <div class="contact-item">
        <svg class="icon" viewBox="0 0 24 24"><circle cx="12" cy="12" r="11" fill="#fff"/><rect x="8" y="6" width="8" height="4" fill="var(--brand-red)"/><rect x="6" y="10" width="12" height="6" rx="1" fill="var(--brand-red)"/><rect x="8" y="14" width="8" height="4" fill="var(--brand-red)"/></svg>
        <span>+64 (0)9 4813905</span>
      </div>
      <div class="contact-item">
        <svg class="icon" viewBox="0 0 24 24"><circle cx="12" cy="12" r="11" fill="#fff"/><rect x="8.5" y="5" width="7" height="14" rx="1.5" fill="var(--brand-red)"/><rect x="10" y="7" width="4" height="8" fill="#fff"/></svg>
        <span>+64 (0)21 968014</span>
      </div>
    </div>
  </div>
</section>

<section class="card card-back">
  <svg class="card-art" viewBox="0 0 700 400">
    <path d="M0 290 Q 470 320 700 96 L700 400 L0 400 Z" fill="var(--brand-blue)"/>
    <path d="M0 308 Q 480 342 700 138 L700 400 L0 400 Z" fill="var(--brand-red)"/>
    <path id="tagline-path" d="M0 302 Q 475 333 700 122" fill="none"/>
    <text class="tagline"><textPath href="#tagline-path" startOffset="66%">Service Excellence</textPath></text>
  </svg>

  <p class="back-brand">HARBOURLINK PF</p>
  <p class="back-web">www.harbourlinkpf.co.nz</p>
  <div class="back-tollfree">
    <p class="tollfree-label">CALL TOLL FREE (NZ ONLY)</p>
    <p class="tollfree-number">0508 391046</p>
  </div>
</section>

</body>
</html>
```